New Business Card for General Contractor Marketing

Need a business card the is more like a marketing promotion of our services
Must be horizontal orientation, One Sided Only, Max font size, Organize the Services
#1 General Contractor for Realtors
Remodels – Renovations – Repairs
Water & Mold Damage Experts
Painting: Interior/ Exterior
Flooring: Wood / LVT / Carpet
Plumbing: Repairs & Upgrades
Electric: Lights & Energy Efficient Upgrades
Kitchen & Bath Remodels
Fast Inspections Repair Billed Thru Escrow
BrightHarborBuilds.com
555-418-2796

Industry/Entity Type

General Contractor

Contact Information for Business Card

One Sided Only: #1 General Contractor for Realtors Remodels – Renovations – Repairs Water & Mold Damage Experts Painting: Interior/ Exterior Flooring: Wood / LVT / Carpet Plumbing: Repairs & Upgrades Electric: Lights & Energy Efficient Upgrades Kitchen & Bath Remodels Fast Inspections Repair Billed Thru Escrow BrightHarborBuilds.com 555-418-2796

Colors
0054AA
0677BA
7BADD7
CADEEF
E8F1F8

Requirements
Must have
• One Sided Only: #1 General Contractor for Realtors Remodels – Renovations – Repairs Water & Mold Damage Experts Painting: Interior/ Exterior Flooring: Wood / LVT / Carpet Plumbing: Repairs & Upgrades Electric: Lights & Energy Efficient Upgrades Kitchen & Bath Remodels Fast Inspections Repair Billed Thru Escrow BrightHarborBuilds.com 555-418-2796

```html
<!DOCTYPE html>
<html lang="en">
<head>
<meta charset="utf-8">
<title>Harborline Remodel – Business Card</title>
<link href="https://fonts.googleapis.com/css2?family=Montserrat:wght@500;600&family=Oswald:wght@500;600;700&display=swap" rel="stylesheet">
<style>
  :root {
    --page-bg: #e9ebee;
    --card-bg: #ffffff;
    --ink: #222426;
    --ink-soft: #2e3133;
    --blue: #3f86e8;
    --grey-strip: #3a3c3f;
    --white: #ffffff;
  }
  * { box-sizing: border-box; margin: 0; padding: 0; }
  html, body { width: 1200px; height: 900px; overflow: hidden; }
  body {
    background: var(--page-bg);
    position: relative;
    font-family: "Montserrat", Arial, sans-serif;
  }
  .card {
    position: absolute;
    left: 75px; top: 150px;
    width: 1050px; height: 600px;
    background: var(--card-bg);
    border-radius: 28px;
    overflow: hidden;
    box-shadow: 0 14px 40px rgba(0,0,0,0.18);
  }
  .service-list {
    position: absolute;
    left: 64px; top: 44px;
    list-style: none;
    font-weight: 600;
    font-size: 25px;
    line-height: 38px;
    color: var(--ink-soft);
    white-space: nowrap;
  }
  .service-list li { position: relative; padding-left: 30px; }
  .service-list li::before {
    content: "";
    position: absolute; left: 0; top: 12px;
    width: 15px; height: 15px; border-radius: 50%;
    background: var(--blue);
  }
  .brand {
    position: absolute;
    right: 60px; top: 48px;
    display: flex; align-items: center; gap: 16px;
  }
  .brand-mark {
    width: 34px; height: 34px; background: var(--blue); flex: none;
  }
  .brand-name {
    font-family: "Oswald", Arial, sans-serif;
    font-weight: 600;
    font-size: 56px;
    letter-spacing: 1px;
    color: var(--blue);
    text-transform: uppercase;
    line-height: 1.05;
    text-align: left;
  }
  .phone-row {
    position: absolute;
    left: 64px; top: 404px;
    display: flex; align-items: center; gap: 22px;
    white-space: nowrap;
  }
  .phone-icon { width: 90px; height: 90px; flex: none; }
  .phone-number {
    font-family: "Oswald", Arial, sans-serif;
    font-weight: 700;
    font-size: 88px;
    line-height: 1;
    color: var(--ink);
    letter-spacing: -1px;
  }
  .footer-bands {
    position: absolute; left: 0; bottom: 0;
    width: 1050px; height: 85px;
  }
  .website {
    position: absolute;
    right: 44px; bottom: 20px;
    font-family: "Oswald", Arial, sans-serif;
    font-weight: 500;
    font-size: 36px;
    line-height: 1.2;
    letter-spacing: 3px;
    color: var(--white);
    text-transform: uppercase;
    white-space: nowrap;
  }
</style>
</head>
<body>
  <section class="card">
    <ul class="service-list">
      <li>#1 General Contractor for Realtors</li>
      <li>Remodels – Renovations – Repairs</li>
      <li>Water &amp; Mold Damage Experts</li>
      <li>Painting: Interior/ Exterior</li>
      <li>Flooring: Wood / LVT / Carpet</li>
      <li>Plumbing: Repairs &amp; Upgrades</li>
      <li>Electric: Lights &amp; Energy Efficient Upgrades</li>
      <li>Kitchen &amp; Bath Remodels</li>
      <li>Fast Inspections Repair Billed Thru Escrow</li>
    </ul>

    <div class="brand">
      <span class="brand-mark"></span>
      <span class="brand-name">Harborline<br>Remodel</span>
    </div>

    <div class="phone-row">
      <svg class="phone-icon" viewBox="0 0 96 96" aria-hidden="true">
        <circle cx="48" cy="48" r="43" fill="none" stroke="var(--blue)" stroke-width="6"/>
        <path d="M24 40 q24 -16 48 0 l-3 8 h-10 l-2 -6 q-9 -3 -18 0 l-2 6 h-10 z" fill="var(--blue)"/>
        <path d="M30 50 h36 l6 20 h-48 z" fill="var(--blue)"/>
        <circle cx="48" cy="61" r="6" fill="none" stroke="var(--white)" stroke-width="3"/>
      </svg>
      <span class="phone-number">555-418-2796</span>
    </div>

    <svg class="footer-bands" viewBox="0 0 1050 85" preserveAspectRatio="none" aria-hidden="true">
      <polygon points="0,47 500,47 485,85 0,85" fill="var(--grey-strip)"/>
      <polygon points="520,0 1050,0 1050,85 485,85" fill="var(--blue)"/>
    </svg>
    <span class="website">BrightHarborBuilds.com</span>
  </section>
</body>
</html>
```